Financial Planning firm focused on serving women 55-65 yrs old needs stationary design

We are rebranding our financial planning firm and our target client is a 55-65 yr old women. We need a stationary design to go with our new logo.

Contact Information: Raymond Kessler, MS, CFP President Harlow Wealth Management 4820 Bramblewood Lane, Suite 317 Estero, FL 33961 ray@harlowwealthmgmt.example phone 239-555-0184

```html
<!DOCTYPE html>
<html lang="en">
<head>
<meta charset="utf-8">
<title>Harlow Wealth Management — Presentation Folder</title>
<link rel="stylesheet" href="https://fonts.googleapis.com/css2?family=Questrial&display=swap">
<style>
  :root {
    --backdrop: #e4e4e4;
    --paper: #ffffff;
    --ocean: #2f6189;
    --sage: #a3b5a0;
    --ink-light: #dfe8f0;
    --fold: rgba(0, 0, 0, 0.08);
  }
  * { margin: 0; padding: 0; box-sizing: border-box; }
  html, body {
    width: 1200px;
    height: 847px;
    overflow: hidden;
    background: var(--backdrop);
    font-family: "Questrial", "Century Gothic", sans-serif;
  }
  .folder-spread {
    position: absolute;
    left: 75px;
    top: 73px;
    width: 1050px;
    height: 700px;
    background: var(--paper);
    box-shadow: 0 6px 24px rgba(0, 0, 0, 0.18);
    overflow: hidden;
  }
  .folder-artwork {
    position: absolute;
    inset: 0;
    width: 100%;
    height: 100%;
  }
  .fold-line {
    position: absolute;
    left: 524px;
    top: 0;
    width: 2px;
    height: 100%;
    background: var(--fold);
  }
  .brand-lockup {
    position: absolute;
    left: 690px;
    top: 82px;
    display: flex;
    align-items: center;
    gap: 12px;
  }
  .brand-mark {
    width: 52px;
    height: 52px;
    border-radius: 50%;
    background: var(--sage);
  }
  .brand-name {
    color: var(--ocean);
    font-size: 22px;
    letter-spacing: 0.5px;
    white-space: nowrap;
  }
  .contact-block {
    position: absolute;
    left: 40px;
    bottom: 40px;
    color: var(--ink-light);
    font-size: 10px;
    line-height: 13px;
  }
  .contact-row {
    display: flex;
    align-items: center;
    gap: 6px;
  }
  .contact-icon {
    width: 10px;
    height: 10px;
    flex: none;
  }
  .contact-address { margin-top: 3px; }
</style>
</head>
<body>
  <main class="folder-spread">
    <svg class="folder-artwork" viewBox="0 0 1050 700" preserveAspectRatio="none" aria-hidden="true">
      <path class="sage-sweep" fill="var(--sage)"
        d="M0,92 C150,172 350,226 525,234 C720,240 900,232 1050,206
           L1050,210 C900,238 720,248 525,244 C350,240 150,198 0,116 Z"/>
      <path class="ocean-field" fill="var(--ocean)"
        d="M0,126 C150,205 350,250 525,254 C720,258 900,246 1050,218 L1050,700 L0,700 Z"/>
    </svg>
    <div class="fold-line"></div>

    <div class="brand-lockup">
      <span class="brand-mark"></span>
      <span class="brand-name">Harlow Wealth Management</span>
    </div>

    <address class="contact-block" style="font-style:normal">
      <div class="contact-row">
        <svg class="contact-icon" viewBox="0 0 10 10"><circle cx="5" cy="5" r="4.5" fill="none" stroke="currentColor" stroke-width="0.8"/><path d="M3.3,2.8 L4.2,2.6 L4.6,3.8 L4,4.3 C4.4,5.1 4.9,5.6 5.7,6 L6.2,5.4 L7.4,5.8 L7.2,6.7 C5.2,6.9 3.1,4.8 3.3,2.8 Z" fill="currentColor"/></svg>
        <span>239-555-0184</span>
      </div>
      <div class="contact-row">
        <svg class="contact-icon" viewBox="0 0 10 10"><circle cx="5" cy="5" r="4.5" fill="none" stroke="currentColor" stroke-width="0.8"/><rect x="3" y="3.5" width="4" height="3.5" fill="currentColor"/></svg>
        <span>239-555-0185</span>
      </div>
      <div class="contact-row">
        <svg class="contact-icon" viewBox="0 0 10 10"><circle cx="5" cy="5" r="4.5" fill="none" stroke="currentColor" stroke-width="0.8"/><rect x="2.8" y="3.4" width="4.4" height="3.2" fill="none" stroke="currentColor" stroke-width="0.7"/><path d="M2.8,3.4 L5,5.2 L7.2,3.4" fill="none" stroke="currentColor" stroke-width="0.7"/></svg>
        <span>ray@harlowwealthmgmt.example</span>
      </div>
      <div class="contact-row">
        <svg class="contact-icon" viewBox="0 0 10 10"><circle cx="5" cy="5" r="4.5" fill="none" stroke="currentColor" stroke-width="0.8"/><circle cx="5" cy="5" r="2.3" fill="none" stroke="currentColor" stroke-width="0.6"/><path d="M2.7,5 H7.3 M5,2.7 V7.3" stroke="currentColor" stroke-width="0.5"/></svg>
        <span>www.harlowwealthmgmt.example</span>
      </div>
      <div class="contact-address">4820 Bramblewood Lane, Suite 317<br>Estero, FL 33961</div>
    </address>
  </main>
</body>
</html>
```